Honeycrisp Apple Moonshine Design

I would like to see if someone can take my design and make it awesome.This is a label for the front of the bottle the size of the label 3" x 5".

Target Market(s)

Alcohol & Spirits

Requirements
Must have
• Must have Photo with man, still and apple. All text must remain fonts can be changed.
Nice to have
• Wow factor

```html
<!DOCTYPE html>
<html lang="en">
<head>
<meta charset="utf-8">
<title>Honeycrisp Apple Shine Label</title>
<link rel="stylesheet" href="https://fonts.googleapis.com/css2?family=Almendra:wght@400;700&family=Fondamento&family=Delius&display=swap">
<style>
  :root {
    --backdrop: #c23a3c;
    --label-white: #ffffff;
    --charcoal: #3d3d3d;
    --label-red: #ec1c24;
    --label-yellow: #f3ec19;
    --cream-white: #ffffff;
    --dot-red: #d5151c;
  }
  html, body {
    margin: 0;
    padding: 0;
    width: 1200px;
    height: 1200px;
    overflow: hidden;
    background: var(--backdrop);
  }
  .canvas {
    position: relative;
    width: 1200px;
    height: 1200px;
  }
  .label {
    position: absolute;
    left: 226px;
    top: 100px;
    width: 749px;
    height: 1000px;
    box-shadow: 0 10px 30px rgba(0,0,0,0.25);
  }
  .label svg { display: block; width: 100%; height: 100%; }
  .edition-text { font-family: 'Almendra', serif; font-weight: 700; font-size: 17px; fill: var(--label-yellow); letter-spacing: 1px; }
  .brand-name { font-family: 'Fondamento', cursive; font-size: 34px; fill: var(--cream-white); letter-spacing: 2px; }
  .flavor-top { font-family: 'Almendra', serif; font-weight: 700; font-size: 26px; fill: var(--cream-white); letter-spacing: 2px; }
  .flavor-mid { font-family: 'Almendra', serif; font-weight: 700; font-size: 19px; fill: var(--cream-white); letter-spacing: 3px; }
  .flavor-main { font-family: 'Almendra', serif; font-weight: 700; font-size: 50px; fill: var(--label-yellow); letter-spacing: 5px; }
  .proof-number { font-family: 'Almendra', serif; font-weight: 700; font-size: 26px; fill: var(--label-red); }
  .proof-word { font-family: 'Almendra', serif; font-weight: 700; font-size: 8px; fill: var(--label-red); letter-spacing: 1px; }
  .abv-text { font-family: 'Almendra', serif; font-weight: 700; font-size: 13px; fill: var(--label-yellow); letter-spacing: 2px; }
  .maker-line { font-family: 'Delius', sans-serif; font-size: 24px; fill: var(--charcoal); letter-spacing: 1.5px; }
  .maker-name { font-family: 'Delius', sans-serif; font-size: 28px; fill: var(--label-red); letter-spacing: 1.5px; }
</style>
</head>
<body>
<main class="canvas">
  <section class="label">
    <svg viewBox="0 0 608 812" xmlns="http://www.w3.org/2000/svg">
      <defs>
        <linearGradient id="photo-tones" x1="0" y1="0" x2="1" y2="1">
          <stop offset="0" stop-color="#7d7468"/>
          <stop offset="0.45" stop-color="#4c5a72"/>
          <stop offset="1" stop-color="#b4683a"/>
        </linearGradient>
        <path id="edition-arc" d="M 126,283 A 178 178 0 0 1 482,283"/>
      </defs>

      <rect class="label-base" x="0" y="0" width="608" height="812" fill="var(--label-white)"/>
      <rect class="red-field" x="0" y="415" width="608" height="305" fill="var(--label-red)"/>
      <rect class="yellow-band" x="0" y="720" width="608" height="92" fill="var(--label-yellow)"/>

      <circle class="emblem-ring" cx="304" cy="283" r="180" fill="none" stroke="var(--charcoal)" stroke-width="40"/>
      <text class="edition-text"><textPath href="#edition-arc" startOffset="50%" text-anchor="middle">Special Edition</textPath></text>

      <rect class="photo-area" role="img" aria-label="Photo of a bearded man in overalls beside a copper still, holding an apple"
        x="200" y="150" width="208" height="240" rx="16" fill="url(#photo-tones)"/>

      <polygon class="ribbon-tail" points="22,340 125,372 90,432 0,418 0,410" fill="var(--charcoal)"/>
      <polygon class="ribbon-tail" points="586,340 483,372 518,432 608,418 608,410" fill="var(--charcoal)"/>
      <path class="ribbon-banner" d="M 75,383 Q 304,410 533,383 L 540,470 Q 304,500 68,470 Z" fill="var(--charcoal)"/>
      <path class="ribbon-fold" d="M 75,390 Q 304,417 533,390" fill="none" stroke="var(--label-white)" stroke-width="1.5"/>

      <circle class="ribbon-dot" cx="133" cy="440" r="12" fill="var(--dot-red)"/>
      <circle class="ribbon-dot" cx="475" cy="440" r="12" fill="var(--dot-red)"/>
      <text class="brand-name" x="304" y="458" text-anchor="middle">TK Hollers</text>

      <text class="flavor-top" x="245" y="553" text-anchor="middle">HONYCRISP</text>
      <text class="flavor-mid" x="247" y="603" text-anchor="middle">APPLE</text>
      <text class="flavor-main" x="243" y="664" text-anchor="middle">SHINE</text>

      <g class="proof-badge">
        <circle cx="428" cy="592" r="46" fill="var(--label-yellow)"/>
        <text class="proof-number" x="428" y="598" text-anchor="middle">60</text>
        <text class="proof-word" x="428" y="611" text-anchor="middle">PROOF</text>
        <text class="abv-text" x="428" y="664" text-anchor="middle">30 ABV</text>
      </g>

      <text class="maker-line" x="304" y="753" text-anchor="middle">Distilled &amp; Bottled By</text>
      <text class="maker-name" x="304" y="791" text-anchor="middle">Pine Ridge Distilling com.</text>
    </svg>
  </section>
</main>
</body>
</html>
```